HLD business cards Dr. Martin Voss

I need a business card designed for our dental office. We are a "general dental" practice.
Looking for a clean, professional but not too fancy design with our logo and contact information required.
front of card is information/standard business card, backside is appt reminder with lines for date and time of appt
doctors name: Dr. Martin Voss DMD
office name: Voss Family Dental
address: 4827 N Birchwell Ave Alder Ridge, OR 97031
phone: 541-555-0173
Contact Information for Business Card
Office name, Doctor name, address, phone number...etc
- White/off white base color, blue and or black lettering

```html
<!DOCTYPE html>
<html lang="en">
<head>
<meta charset="utf-8">
<title>Voss Family Dental – Business Cards</title>
<link rel="stylesheet" href="https://fonts.googleapis.com/css2?family=Cinzel:wght@600&family=Tinos:wght@700&family=Roboto:wght@400;500&display=swap">
<style>
  :root {
    --backdrop: #2d2d2d;
    --brand-blue: #0d4a93;
    --brand-blue-deep: #0a3d7e;
    --paper: #efefef;
    --paper-shade: #e2e2e2;
    --ink: #3c4249;
    --ink-soft: #4a4f55;
    --slate: #50565c;
    --white: #ffffff;
  }
  * { margin: 0; padding: 0; box-sizing: border-box; }
  html, body { width: 1200px; height: 1138px; overflow: hidden; }
  body { background: var(--backdrop); position: relative; font-family: "Roboto", Arial, sans-serif; }

  .card { position: absolute; border-radius: 16px; overflow: hidden; }

  .card-front {
    left: 274px; top: 186px; width: 623px; height: 376px;
    background: linear-gradient(180deg, var(--brand-blue) 0%, var(--brand-blue-deep) 100%);
  }
  .front-mark {
    position: absolute; left: 256px; top: 280px; top: 92px;
    width: 110px; height: 110px; border-radius: 50%;
    background: #0b3870;
  }
  .front-name {
    position: absolute; left: 0; right: 0; top: 238px;
    text-align: center;
    font-family: "Cinzel", Georgia, serif; font-weight: 600;
    color: #e6e9ee; line-height: 1;
  }
  .front-name-main { display: block; font-size: 34px; letter-spacing: 1px; }
  .front-name-sub { display: block; font-size: 17px; letter-spacing: 9px; margin-top: 6px; padding-left: 9px; }

  .card-back {
    left: 276px; top: 608px; width: 618px; height: 374px;
    background: linear-gradient(180deg, var(--paper) 0%, var(--paper-shade) 100%);
  }
  .back-brand {
    position: absolute; left: 29px; top: 56px;
    display: flex; align-items: center; gap: 22px;
  }
  .back-brand-dot { width: 70px; height: 70px; border-radius: 50%; background: var(--brand-blue); }
  .back-brand-name {
    font-family: "Cinzel", Georgia, serif; font-weight: 600;
    color: var(--ink-soft); line-height: 1; text-align: center;
  }
  .back-brand-main { display: block; font-size: 33px; letter-spacing: 0.5px; }
  .back-brand-sub { display: block; font-size: 16px; letter-spacing: 9px; margin-top: 6px; padding-left: 9px; }

  .doctor { position: absolute; left: 29px; top: 228px; }
  .doctor-name {
    font-family: "Tinos", "Times New Roman", serif; font-weight: 700;
    font-size: 24px; color: var(--ink);
  }
  .doctor-role { font-size: 16px; color: var(--ink-soft); margin-top: 2px; }

  .contact { position: absolute; left: 352px; top: 230px; font-size: 16px; line-height: 24px; color: var(--ink-soft); }
  .contact-row { display: flex; gap: 8px; }
  .contact-row svg { flex: none; margin-top: 5px; }
  .contact-phone { color: var(--brand-blue); font-weight: 500; }

  .footer-bands { position: absolute; left: 0; bottom: 0; }
  .footer-label {
    position: absolute; right: 58px; bottom: 14px;
    font-family: "Cinzel", Georgia, serif; font-weight: 600;
    font-size: 17px; color: var(--white); letter-spacing: 0.5px;
  }
</style>
</head>
<body>
  <section class="card card-front" aria-label="Card front">
    <div class="front-mark"></div>
    <div class="front-name">
      <span class="front-name-main">VOSS FAMILY</span>
      <span class="front-name-sub">DENTAL</span>
    </div>
  </section>

  <section class="card card-back" aria-label="Card back">
    <div class="back-brand">
      <div class="back-brand-dot"></div>
      <div class="back-brand-name">
        <span class="back-brand-main">VOSS FAMILY</span>
        <span class="back-brand-sub">DENTAL</span>
      </div>
    </div>

    <div class="doctor">
      <div class="doctor-name">Dr. Martin Voss DMD</div>
      <div class="doctor-role">Senior Dentist</div>
    </div>

    <div class="contact">
      <div class="contact-row">
        <svg width="18" height="14" viewBox="0 0 18 14" aria-hidden="true">
          <path d="M1 5 Q9 -1 17 5 L15 7 L12 5 L12 4 Q9 3 6 4 L6 5 L3 7 Z" fill="var(--brand-blue)"/>
          <rect x="4" y="7" width="10" height="6" rx="1" fill="var(--brand-blue)"/>
        </svg>
        <span class="contact-phone">541-555-0173</span>
      </div>
      <div class="contact-row">
        <svg width="18" height="16" viewBox="0 0 18 16" aria-hidden="true">
          <path d="M9 1 C5.5 1 3.5 3.5 3.5 6 C3.5 9.5 9 15 9 15 C9 15 14.5 9.5 14.5 6 C14.5 3.5 12.5 1 9 1 Z" fill="var(--brand-blue)"/>
          <circle cx="9" cy="6" r="2.2" fill="var(--paper)"/>
        </svg>
        <span>4827 N Birchwell Ave Alder<br>Ridge, OR 97031</span>
      </div>
    </div>

    <svg class="footer-bands" width="618" height="48" viewBox="0 0 618 48" aria-hidden="true">
      <rect x="0" y="32" width="380" height="16" fill="var(--slate)"/>
      <path d="M336 0 L618 0 L618 48 L300 48 Z" fill="var(--brand-blue)"/>
    </svg>
    <div class="footer-label">VOSS FAMILY DENTAL</div>
  </section>
</body>
</html>
```